4R Capital business cards for a tech VC

We're starting a new Venture Capital that is focusing on bringing the best start ups from Israel to NYC
We need a business cards template for this that gives the sense of an entrepreneurial look
I don't want any religious signs on this even thought it's Israel
I'm looking for a techi feeling but not too crazy
The card should probably be in the same light blue as the logo and the logo in white

Target Market(s)

Investors

Industry/Entity Type

Tech

Contact Information for Business Card

The card needs to look slick and entrepreneurship like
The VC is focused on NYC and Tel Aviv so could be great to show something on the back side that is like NYC skyline or something like that
You can see the logo attached

Colors
0455a3
3276b5
85acd3
cedeed
eaf1f7

Requirements
Must have
• A very cool looking business card that shows we're a cutting edge tech VC with a focus on bringing start ups from Tel Aviv and leveraging the NYC ecosystem
Nice to have
• NYC skyline can be cool , maybe something that is connected to Tel Aviv

```html
<!DOCTYPE html>
<html lang="en">
<head>
<meta charset="UTF-8">
<title>4R Capital – Business Card</title>
<link rel="stylesheet" href="https://fonts.googleapis.com/css2?family=Open+Sans:wght@400;600;700&display=swap">
<style>
  :root {
    --stage: #e4e4e4;
    --card-white: #ffffff;
    --ink-dark: #1f2329;
    --ink-grey: #555a60;
    --brand-blue: #1f8ad0;
    --brand-deep: #0455a3;
    --brand-mid: #3276b5;
    --city-a: #3a3e45;
    --city-b: #23272d;
  }
  * { box-sizing: border-box; margin: 0; padding: 0; }
  html, body {
    width: 1200px; height: 864px; overflow: hidden;
    background: var(--stage);
    font-family: "Open Sans", Arial, sans-serif;
  }
  .stage {
    position: relative; width: 1200px; height: 864px;
    display: flex; flex-direction: column; align-items: center; justify-content: center; gap: 36px;
  }
  .card {
    position: relative; width: 600px; height: 343px; overflow: hidden;
    box-shadow: 0 6px 18px rgba(0,0,0,.22);
  }
  /* Front */
  .card-front {
    display: flex; align-items: center; justify-content: center;
  }
  .city-backdrop {
    position: absolute; inset: 0;
    background: linear-gradient(160deg, var(--city-a) 0%, var(--city-b) 100%);
  }
  .front-wordmark {
    position: relative; color: #ffffff;
    font-weight: 700; font-size: 54px; letter-spacing: 3px;
  }
  /* Back */
  .card-back { background: var(--card-white); }
  .back-wordmark {
    position: absolute; left: 40px; top: 145px; width: 205px;
    color: var(--brand-blue); font-weight: 700; font-size: 36px; letter-spacing: 1px;
    text-align: center;
  }
  .divider {
    position: absolute; left: 268px; top: 78px; width: 1.5px; height: 175px;
    background: var(--brand-blue);
  }
  .contact { position: absolute; left: 292px; top: 78px; color: var(--ink-grey); }
  .contact-name { color: var(--brand-deep); font-weight: 700; font-size: 20px; line-height: 1.1; }
  .contact-role { font-size: 13px; margin-bottom: 14px; }
  .contact-address { font-size: 12.5px; line-height: 1.4; margin-bottom: 12px; }
  .contact-list { list-style: none; font-size: 12.5px; line-height: 1.45; }
  .contact-list li { display: flex; align-items: center; gap: 8px; }
  .contact-list svg { width: 12px; height: 12px; flex: none; }
  .bottom-band { position: absolute; left: 0; bottom: 0; width: 600px; height: 48px; }
</style>
</head>
<body>
<main class="stage">
  <section class="card card-front" aria-label="Card front">
    <div class="city-backdrop" role="img" aria-label="Dark-toned aerial photograph of the New York City skyline"></div>
    <div class="front-wordmark">4R Capital</div>
  </section>

  <section class="card card-back" aria-label="Card back">
    <div class="back-wordmark">4R Capital</div>
    <div class="divider"></div>
    <div class="contact">
      <p class="contact-name">Daniel Reyes</p>
      <p class="contact-role">President</p>
      <p class="contact-address">Street Name Avenue, Suite 000<br>State, Zip Code, Country</p>
      <ul class="contact-list">
        <li><svg viewBox="0 0 12 12"><path d="M2 1l2 0 1 3-1.5 1a6 6 0 0 0 3.5 3.5L8 7l3 1v2a1 1 0 0 1-1 1A9 9 0 0 1 1 2a1 1 0 0 1 1-1z" fill="#1f8ad0"/></svg>01 012-345-6789</li>
        <li><svg viewBox="0 0 12 12"><rect x="3" y="0.7" width="6" height="10.6" rx="1" fill="none" stroke="#1f8ad0" stroke-width="1.2"/><circle cx="6" cy="9.3" r=".7" fill="#1f8ad0"/></svg>01 012-345-6780</li>
        <li><svg viewBox="0 0 12 12"><rect x=".7" y="2.2" width="10.6" height="7.6" fill="none" stroke="#1f8ad0" stroke-width="1.2"/><path d="M.7 2.2L6 6.5l5.3-4.3" fill="none" stroke="#1f8ad0" stroke-width="1.2"/></svg>info@yourwebsite.com</li>
        <li><svg viewBox="0 0 12 12"><circle cx="6" cy="6" r="5.2" fill="none" stroke="#1f8ad0" stroke-width="1.2"/><ellipse cx="6" cy="6" rx="2.2" ry="5.2" fill="none" stroke="#1f8ad0" stroke-width="1"/><path d="M.8 6h10.4" stroke="#1f8ad0" stroke-width="1"/></svg>yourwebsite.com</li>
      </ul>
    </div>
    <svg class="bottom-band" viewBox="0 0 600 48" preserveAspectRatio="none" aria-hidden="true">
      <polygon points="0,36 315,36 312,48 0,48" fill="#1f8ad0"/>
      <polygon points="0,42 600,42 600,48 0,48" fill="#1f8ad0"/>
      <polygon points="322,22 600,6 600,48 312,48" fill="#1f76c4"/>
      <polygon points="315,36 322,22 324,22 317,36" fill="#ffffff"/>
    </svg>
  </section>
</main>
</body>
</html>
```